SilverLedgerOak - Double Sided Business Card

We are looking for design options or our business cards. We are a Business Solutions and HR solutions Provider - the theme is business, for this card.

Our brand colours are represented within our logo.

Details needed to be put on the front of the business card are:

Employees name: [Sample Name]
Role: [Sample Role]

Address: Suite 4 - Level 3/48 Halloran Avenue Marrowdale NSW 2186
M: 0000 000 000
P: 1300 847 213
F: 1300 847 286
E: sample@silverledgeroak.com.au
www.silverledgeroak.com.au
Updates

Reason: Hello, could we please increase our deadline by 5 days. Thanking you, Tess

Target Market(s)

Business Owners, also Candidates looking for Employment

Industry/Entity Type

Business

Contact Information for Business Card

Role: [Sample Role]

M: 0000 000 000
P: 1300 847 213
F: 1300 847 286

Font styles to use
Sans Serif

Colors
3276b5
3176b5
0455a3
85abd2
cfdeed
ffffff
000000
1b1b1b
757575

Requirements
Must have
• Details needed to be put on the front of the business card are:
• Employees name: [Sample Name]
• Role: [Sample Role]
• Address: Suite 4 - Level 3/48 Halloran Avenue Marrowdale NSW 2186
• M: 0000 000 000
• P: 1300 847 213
• F: 1300 847 286
• E: sample@silverledgeroak.com.au
• www.silverledgeroak.com.au
Nice to have
• Simplicity, clean and professional.

```html
<!DOCTYPE html>
<html lang="en">
<head>
<meta charset="utf-8">
<title>SilverLedgerOak – Business Card</title>
<link rel="stylesheet" href="https://fonts.googleapis.com/css2?family=Ubuntu:wght@400;500;700&display=swap">
<style>
  :root {
    --stage: #3c3c3c;
    --card: #1b1b1b;
    --ink-white: #ffffff;
    --ink-light: #cfdeed;
    --accent: #4a9fe0;
    --brand-blue: #0455a3;
    --brand-mid: #3276b5;
    --emboss: #2c2c2c;
  }
  * { margin: 0; padding: 0; box-sizing: border-box; }
  html, body {
    width: 799px; height: 1200px; overflow: hidden;
    background: var(--stage);
    font-family: "Ubuntu", sans-serif;
  }
  .card {
    position: absolute; left: 80px;
    width: 640px; height: 366px;
    background: var(--card);
    border-radius: 4px;
    overflow: hidden;
    box-shadow: 0 18px 40px rgba(0,0,0,.45);
  }
  .card--back { top: 120px; }
  .card--front { top: 712px; }

  .back-mark {
    position: absolute; inset: 0;
    display: flex; align-items: center; justify-content: center;
    font-size: 40px; font-weight: 700; color: var(--emboss);
    letter-spacing: .5px;
  }

  .waves { position: absolute; left: 0; top: 0; width: 640px; height: 366px; }

  .brand { position: absolute; left: 34px; top: 52px; width: 310px; }
  .brand__name {
    display: flex; align-items: center; gap: 10px;
    font-size: 30px; font-weight: 700; color: var(--ink-white);
  }
  .brand__square { width: 20px; height: 20px; background: var(--accent); }
  .brand__rule { height: 1px; background: var(--ink-light); margin: 10px 0 6px; opacity: .8; }
  .brand__tagline { font-size: 10.5px; font-weight: 500; color: var(--ink-white); }

  .person {
    position: absolute; right: 34px; top: 56px; text-align: right;
    color: var(--ink-white);
  }
  .person__name { font-size: 24px; font-weight: 500; color: var(--accent); }
  .person__role { font-size: 13px; margin-top: 3px; }
  .person__line {
    display: flex; justify-content: flex-end; align-items: center; gap: 8px;
    font-size: 14px; margin-top: 7px;
  }
  .person__line--first { margin-top: 14px; }

  .office {
    position: absolute; right: 34px; bottom: 16px; text-align: right;
    color: var(--ink-white); font-size: 15px; line-height: 1.3;
  }
  .office__line { display: flex; justify-content: flex-end; align-items: center; gap: 8px; }
  .office__address { margin-top: 2px; }

  .icon { width: 13px; height: 13px; flex: none; }
</style>
</head>
<body>

<section class="card card--back" aria-label="Card back">
  <div class="back-mark">SilverLedgerOak</div>
</section>

<section class="card card--front" aria-label="Card front">
  <svg class="waves" viewBox="0 0 640 366" aria-hidden="true">
    <path d="M0,150 C200,160 420,198 640,204 L640,213 C420,210 200,172 0,164 Z" fill="var(--brand-mid)"/>
    <path d="M0,178 C220,194 420,226 640,226 L640,366 L0,366 Z" fill="var(--brand-blue)"/>
    <path d="M0,198 C200,214 420,244 640,236 L640,244 C420,256 200,232 0,220 Z" fill="var(--card)"/>
  </svg>

  <div class="brand">
    <div class="brand__name"><span class="brand__square"></span>SilverLedgerOak</div>
    <div class="brand__rule"></div>
    <div class="brand__tagline">Guiding growing firms towards their strongest, steadiest future</div>
  </div>

  <div class="person">
    <div class="person__name">Sample Name</div>
    <div class="person__role">Managing Director</div>
    <div class="person__line person__line--first">0000 000 000
      <svg class="icon" viewBox="0 0 12 12"><rect x="3" y="0.5" width="6" height="11" rx="1" fill="none" stroke="var(--accent)"/><circle cx="6" cy="9.5" r=".8" fill="var(--accent)"/></svg>
    </div>
    <div class="person__line">sample@silverledgeroak.com.au
      <svg class="icon" viewBox="0 0 12 12"><rect x=".5" y="2" width="11" height="8" fill="none" stroke="var(--accent)"/><path d="M.5,2 L6,6.5 L11.5,2" fill="none" stroke="var(--accent)"/></svg>
    </div>
  </div>

  <div class="office">
    <div class="office__line">1300 847 213
      <svg class="icon" viewBox="0 0 12 12"><path d="M1,4 C1,2 3,1 6,1 C9,1 11,2 11,4 L8.5,4.5 L8,3 L4,3 L3.5,4.5 Z M2.5,6 L9.5,6 L10.5,11 L1.5,11 Z" fill="var(--ink-white)"/></svg>
    </div>
    <div class="office__line">1300 847 286
      <svg class="icon" viewBox="0 0 12 12"><rect x="3" y="1" width="6" height="3" fill="var(--ink-white)"/><rect x="1" y="4.5" width="10" height="4.5" fill="var(--ink-white)"/><rect x="3" y="8" width="6" height="3" fill="none" stroke="var(--ink-white)"/></svg>
    </div>
    <div class="office__line">www.silverledgeroak.com.au
      <svg class="icon" viewBox="0 0 12 12"><circle cx="6" cy="6" r="5.2" fill="none" stroke="var(--ink-white)"/><ellipse cx="6" cy="6" rx="2.2" ry="5.2" fill="none" stroke="var(--ink-white)"/><path d="M.8,6 H11.2" stroke="var(--ink-white)"/></svg>
    </div>
    <div class="office__address">Suite 4 - Level 3/48 Halloran Avenue<br>Marrowdale NSW 2186</div>
  </div>
</section>

</body>
</html>
```